Pedicure Menu with 8 Scent Options

This design will be for a single page menu (front/back) that will display multiple different scent variations of a product. The purpose of this menu is to display to clients and show them the available options and benefits of each option.
The menu will be double sided.
The front page will include a header including brand logo and product name, and a total of 8 different scents including imagery and descriptive text.
The design should include the text provided for each scent. The design should have a layout that is structured/organized, easy to read, and has bright imagery that represents each scent.
An example is a modular layout using boxes that highlight a different scent within each box. Lavender scent should include aesthetic images of lavender flower and/or the color purple.
The back page will include brand logo, overall product description, and additional brief text that explains each step of the product.
The final size of the design should be 8.5"x11", produced in InDesign format, with all layers editable for future changes.
NOTE: Please carefully review the attached design brief that includes additional information, and all necessary text to include in the design.
Target Market(s)
Beauty/Spa Clients
Industry/Entity Type
Beauty
Requirements
Must have
- Bright and Vivid Imagery/Illustrations
Nice to have
- Background design that utilizes, lines, shapes, or other elements.

```html
<!DOCTYPE html>
<html lang="en">
<head>
<meta charset="utf-8">
<title>Lumora Pedicure Menu</title>
<link href="https://fonts.googleapis.com/css2?family=Montserrat:wght@400;500;600;700;800;900&display=swap" rel="stylesheet">
<style>
:root{
  --backdrop:#d3d4d6;
  --paper:#fffdf6;
  --brand-pink:#d6405f;
  --brand-purple:#8a2bb0;
  --footer-red:#c5463f;
  --ink:#1d1d1d;
  --white:#ffffff;
  --lavender-a:#7a56ad;--lavender-b:#9d2cb9;
  --jasmine-a:#4b7a1c;--jasmine-b:#80aa3c;
  --mandarin-a:#f0761e;--mandarin-b:#f9b02b;
  --rose-a:#ea1a52;--rose-b:#28100f;
  --cucumber-a:#2c5a29;--cucumber-b:#7c9c42;
  --mint-a:#1ca34d;--mint-b:#1e5a2e;
  --tea-a:#161612;--tea-b:#8d8a73;
  --honey-a:#df5f2a;--honey-b:#f9b41d;
  --soak-a:#f0761e;--soak-b:#f9b02b;
  --scrub-a:#7a56ad;--scrub-b:#9d2cb9;
  --mud-a:#ea1a52;--mud-b:#28100f;
  --lotion-a:#1ca34d;--lotion-b:#1e5a2e;
}
*{box-sizing:border-box;margin:0;padding:0}
html,body{width:1200px;height:787px;overflow:hidden}
body{background:var(--backdrop);font-family:"Montserrat",Arial,sans-serif;position:relative}

.page{position:absolute;top:88px;width:473px;height:612px;background:var(--paper);overflow:hidden}
.page--front{left:106px}
.page--back{left:621px}

.floral-top,.floral-bottom{position:absolute;left:0;width:100%}
.floral-top{top:0;height:160px;
  background:
    radial-gradient(circle at 8% 40%,rgba(243,150,70,.35),transparent 28%),
    radial-gradient(circle at 33% 12%,rgba(214,64,95,.30),transparent 22%),
    radial-gradient(circle at 62% 10%,rgba(243,150,70,.30),transparent 22%),
    radial-gradient(circle at 92% 12%,rgba(175,190,110,.35),transparent 20%),
    radial-gradient(circle at 88% 75%,rgba(245,205,30,.30),transparent 25%);}
.floral-bottom{bottom:30px;height:95px;
  background:
    radial-gradient(circle at 6% 40%,rgba(245,205,30,.35),transparent 28%),
    radial-gradient(circle at 35% 55%,rgba(243,150,70,.30),transparent 26%),
    radial-gradient(circle at 63% 70%,rgba(214,64,95,.30),transparent 20%),
    radial-gradient(circle at 90% 55%,rgba(90,190,180,.35),transparent 26%);}

.brand{position:absolute;left:0;top:88px;width:100%;text-align:center}
.brand-name{display:block;font-weight:700;font-size:40px;line-height:1;color:var(--brand-purple);letter-spacing:1px}
.brand-tag{display:block;margin-top:6px;font-size:8px;letter-spacing:2px;color:var(--ink);font-weight:500}

.scent-card{position:absolute;width:219px;height:78px}
.scent-band{position:absolute;left:0;top:5px;width:219px;height:68px;border-radius:14px;padding:9px 7px 0 90px;color:var(--white)}
.scent-photo{position:absolute;left:9px;top:0;width:78px;height:78px;border-radius:50%;border:3px solid var(--white);box-shadow:0 0 0 1px rgba(0,0,0,.2)}
.scent-title{font-size:11.5px;font-weight:600;line-height:1;margin-bottom:3px;letter-spacing:.2px}
.scent-text{font-size:5.1px;line-height:1.26;font-weight:500;text-align:justify}

.lavender .scent-band{background:linear-gradient(90deg,var(--lavender-a),var(--lavender-b))}
.lavender .scent-photo{background:radial-gradient(circle,#a28acc,#f4f0fa 70%)}
.jasmine .scent-band{background:linear-gradient(90deg,var(--jasmine-a),var(--jasmine-b))}
.jasmine .scent-photo{background:radial-gradient(circle,#dfe9d4,#fbfcf8 70%)}
.mandarin .scent-band{background:linear-gradient(90deg,var(--mandarin-a),var(--mandarin-b))}
.mandarin .scent-photo{background:radial-gradient(circle,#f3892a,#fff6ec 70%)}
.rose .scent-band{background:linear-gradient(90deg,var(--rose-a),var(--rose-b))}
.rose .scent-photo{background:radial-gradient(circle,#c51f2c,#fbeeee 68%)}
.cucumber .scent-band{background:linear-gradient(90deg,var(--cucumber-a),var(--cucumber-b))}
.cucumber .scent-photo{background:radial-gradient(circle,#f1a55a,#eef5e6 70%)}
.mint .scent-band{background:linear-gradient(90deg,var(--mint-a),var(--mint-b))}
.mint .scent-photo{background:radial-gradient(circle,#3e8a32,#f2f8ee 70%)}
.tea .scent-band{background:linear-gradient(90deg,var(--tea-a),var(--tea-b))}
.tea .scent-photo{background:radial-gradient(circle,#4d5a33,#f3f4ee 70%)}
.honey .scent-band{background:linear-gradient(90deg,var(--honey-a),var(--honey-b))}
.honey .scent-photo{background:radial-gradient(circle,#f4c04a,#fbfaf6 68%)}

.col-1{left:14px}.col-2{left:240px}
.row-1{top:152px}.row-2{top:241px}.row-3{top:331px}.row-4{top:421px}

.site-footer{position:absolute;left:0;bottom:0;width:100%;height:28px;background:var(--footer-red);color:var(--white);font-size:8.5px;font-weight:600;letter-spacing:2.6px;text-align:center;line-height:28px}

.intro{position:absolute;left:17px;top:172px;width:440px;color:var(--brand-pink);font-size:8.6px;font-weight:600;line-height:1.3;text-align:justify}
.menu-heading{position:absolute;left:17px;top:212px;line-height:.9}
.menu-heading .pick{display:block;font-size:21px;font-weight:900;color:var(--brand-pink)}
.menu-heading .pedicure{display:block;font-size:34px;font-weight:900;color:var(--brand-purple)}
.steps-caption{position:absolute;left:20px;top:272px;font-size:12px;font-weight:600;color:var(--ink)}

.step-card{position:absolute;width:218px;height:78px}
.step-band{position:absolute;left:0;top:13px;width:218px;height:52px;border-radius:13px;padding:6px 6px 0 89px;color:var(--white)}
.step-photo{position:absolute;left:9px;top:0;width:78px;height:78px;border-radius:50%;border:2px solid var(--white);box-shadow:0 0 0 1px rgba(0,0,0,.2)}
.step-number{position:absolute;left:7px;top:25px;width:28px;height:28px;border-radius:50%;color:var(--white);font-size:15px;font-weight:800;text-align:center;line-height:28px;z-index:2}
.step-title{font-size:11.5px;font-weight:600;line-height:1.1}
.step-text{font-size:10px;font-weight:400;line-height:1.2}

.soak .step-band,.soak .step-number{background:linear-gradient(90deg,var(--soak-a),var(--soak-b))}
.soak .step-photo{background:radial-gradient(circle,#e8b99c,#f7ece3 75%)}
.scrub .step-band,.scrub .step-number{background:linear-gradient(90deg,var(--scrub-a),var(--scrub-b))}
.scrub .step-photo{background:radial-gradient(circle,#e3b393,#f4ede8 75%)}
.mud .step-band,.mud .step-number{background:linear-gradient(90deg,var(--mud-a),var(--mud-b))}
.mud .step-photo{background:radial-gradient(circle,#9c7b5c,#2c3448 80%)}
.lotion .step-band,.lotion .step-number{background:linear-gradient(90deg,var(--lotion-a),var(--lotion-b))}
.lotion .step-photo{background:radial-gradient(circle,#e6b498,#f5ece6 75%)}

.step-col-1{left:17px}.step-col-2{left:241px}
.step-row-1{top:298px}.step-row-2{top:384px}
</style>
</head>
<body>

<section class="page page--front">
  <div class="floral-top" role="img" aria-label="Colourful line-art mandala flowers along the top edge"></div>
  <div class="floral-bottom" role="img" aria-label="Colourful line-art mandala flowers along the bottom edge"></div>

  <header class="brand">
    <span class="brand-name">Lumora</span>
    <span class="brand-tag">BEAUTY &amp; SPA</span>
  </header>

  <article class="scent-card lavender col-1 row-1">
    <div class="scent-band">
      <h2 class="scent-title">LAVENDER</h2>
      <p class="scent-text">Melt away the stresses of the day with a delicate, sweet smell that is floral and woody at the same time. Lavender is a calming scent for relaxation that puts us in a better mood and helps create a sense of tranquility and peacefulness.</p>
    </div>
    <div class="scent-photo" role="img" aria-label="Sprigs of purple lavender flowers"></div>
  </article>

  <article class="scent-card jasmine col-2 row-1">
    <div class="scent-band">
      <h2 class="scent-title">JASMINE</h2>
      <p class="scent-text">Embrace the warmth of a rich and sensual floral scent that boosts your energy levels and helps make your day better and brighter. A symbol of purity, love, and beauty Jasmine helps to reduce exhaustion, nervousness, and stress</p>
    </div>
    <div class="scent-photo" role="img" aria-label="White jasmine blossoms with green leaves"></div>
  </article>

  <article class="scent-card mandarin col-1 row-2">
    <div class="scent-band">
      <h2 class="scent-title">MANDARIN</h2>
      <p class="scent-text">Uplift your senses with a fruity and sweet aroma that promotes clarity, radiance and a smooth, even skin tone. A citrus blend of essential oils works great to polish dull skin, reduce wrinkles, and correct spots</p>
    </div>
    <div class="scent-photo" role="img" aria-label="Fresh mandarin oranges with leaves and peeled segments"></div>
  </article>

  <article class="scent-card rose col-2 row-2">
    <div class="scent-band">
      <h2 class="scent-title">ROSE</h2>
      <p class="scent-text">Fall in love with a delicate floral twist of spicy and sweet that nourishes your skin and calms the mind. Essential oils help to reduce fine lines and protect the skin from UV damage.</p>
    </div>
    <div class="scent-photo" role="img" aria-label="A single red rose with leaves"></div>
  </article>

  <article class="scent-card cucumber col-1 row-3">
    <div class="scent-band">
      <h2 class="scent-title">CUCUMBER MELON</h2>
      <p class="scent-text">Melt away the stresses of the day with a delicate, sweet smell that is floral and woody at the same time. Lavender is a calming scent for relaxation that puts us in a better mood and helps create a sense of tranquility and peacefulness.</p>
    </div>
    <div class="scent-photo" role="img" aria-label="Sliced cucumber and cantaloupe melon wedges"></div>
  </article>

  <article class="scent-card mint col-2 row-3">
    <div class="scent-band">
      <h2 class="scent-title">MINT</h2>
      <p class="scent-text">Rejuvenate your body with a cool mix of peppermint and spearmint that prevents skin damage, alleviates inflamed skin, and acts as a splash of tonic for the senses. Infused with eucalyptus to leave you clean, cool, and crisp.</p>
    </div>
    <div class="scent-photo" role="img" aria-label="Bunch of fresh green mint leaves"></div>
  </article>

  <article class="scent-card tea col-1 row-4">
    <div class="scent-band">
      <h2 class="scent-title">GREEN-TEA</h2>
      <p class="scent-text">Restore a sense of serenity with fragrant green tea extract that helps to relax the mind, reduces redness and swelling, and leaves the skin feeling hydrated, silky, and smooth. A natural detoxification that will supplies abundant moisture to the skin.</p>
    </div>
    <div class="scent-photo" role="img" aria-label="Green tea leaves beside dried loose leaf tea"></div>
  </article>

  <article class="scent-card honey col-2 row-4">
    <div class="scent-band">
      <h2 class="scent-title">MILK &amp; HONEY</h2>
      <p class="scent-text">Discover one of nature's most luxurious skin cleansers and softeners. Creamy milk is full of rich essential vitamins that supply abundant moisture and improves skin elasticity. Sweet honey contains antioxidants and other nutrients that slow down skin aging.</p>
    </div>
    <div class="scent-photo" role="img" aria-label="Bottle of milk, jar of honey and honeycomb"></div>
  </article>

  <footer class="site-footer">WWW.LUMORASPA.COM</footer>
</section>

<section class="page page--back">
  <div class="floral-top" role="img" aria-label="Colourful line-art mandala flowers along the top edge"></div>
  <div class="floral-bottom" role="img" aria-label="Colourful line-art mandala flowers along the bottom edge"></div>

  <header class="brand">
    <span class="brand-name">Lumora</span>
    <span class="brand-tag">BEAUTY &amp; SPA</span>
  </header>

  <p class="intro">Lumora Deluxe Pedicure 4-Step will transform your pedicure experience and immerse your senses into a floral paradise designed to rejuvenate your body. Sit back, relax, and enjoy.</p>

  <h1 class="menu-heading"><span class="pick">PICK YOUR</span><span class="pedicure">PEDICURE</span></h1>
  <p class="steps-caption">EACH BOX CONTAINS 4 ESSENTIAL STEPS</p>

  <article class="step-card soak step-col-1 step-row-1">
    <div class="step-band">
      <h3 class="step-title">SALT SOAK</h3>
      <p class="step-text">Detoxifies and deodorizes your feet</p>
    </div>
    <div class="step-photo" role="img" aria-label="Hands rubbing bath salt onto a foot"></div>
    <span class="step-number">1</span>
  </article>

  <article class="step-card scrub step-col-2 step-row-1">
    <div class="step-band">
      <h3 class="step-title">SUGAR SCRUB</h3>
      <p class="step-text">Gently exfoliates dead skin.</p>
    </div>
    <div class="step-photo" role="img" aria-label="Feet being scrubbed with sugar during a spa treatment"></div>
    <span class="step-number">2</span>
  </article>

  <article class="step-card mud step-col-1 step-row-2">
    <div class="step-band">
      <h3 class="step-title">MUD MASK</h3>
      <p class="step-text">Cleanses pores for smoother skin.</p>
    </div>
    <div class="step-photo" role="img" aria-label="Mud mask applied to feet beside candles"></div>
    <span class="step-number">3</span>
  </article>

  <article class="step-card lotion step-col-2 step-row-2">
    <div class="step-band">
      <h3 class="step-title">MASSAGE LOTION</h3>
      <p class="step-text">Hydrates and soothes skin</p>
    </div>
    <div class="step-photo" role="img" aria-label="Hands massaging lotion into a foot"></div>
    <span class="step-number">4</span>
  </article>

  <footer class="site-footer">WWW.LUMORASPA.COM</footer>
</section>

</body>
</html>
```